Business Card Design - Furniture Retail

Open to both Single or double sided design

We are launching a online ecommerce store that sells Scandinavian/Danish style of furniture in Australia.

We aspire to provide stylish but classic and designers' selection of furniture to the Australia public at affordable price. For the style of the furniture we are selling, please see the following links:

https://www.filecrate.example/sh/qk3mzr8wlp/BXTpLnR4vQ7cYdHs?dl=0

The style of the design we are looking for is clean, simple that look Scandinavian/Danish but yet it is timeless classic.

Aspiring Design
http://www.lindmora.com
http://tobyquell.com.au/
http://vekt.furniture/
http://www.olvo.com/
Updates

Please display the card on normal angle for both front and back instead of funny angle. Please keep it display when displaying the design of the business cards so that we can focus on the designs rather than being confused by the unnecessary stuffs like the hands or background

I think there is already enough curve line on the logo itself so anything extra of the curve on the business card would be really unnecessary. Please avoid using any of the extra curve line on the business card, other than the logo itself. Thanks

Regular card and give them a matt celloglaze to create texture on card that makes it looked luxury and expensive.

Please display design on normal angle! Please only use white colour in the background (not the business card but the referring to the submission) rather than anything fancy so that we can focus on the design.

Target Market(s)

High end market consumers who are financially capable and who has good taste and appreciate good design

aged between 28 - 45 white collars professional/businessmen who live in metropolitan areas

Industry/Entity Type

Business

Font styles to use
Serif
Sans Serif

Requirements
Must have
• Regular card and give them a matt celloglaze to create texture on card that makes it looked luxury and expensive.

Please use the logo from the uploaded files

Company Name: Milo Verhagen
Name: Milo Reeb
Phone: +614 27 305 641
Website: www.miloverhagen.com.au
Email: milo@miloverhagen.com.au
Nice to have
• Colour is not limited to black and white
Should not have
• The concept photos of the furniture should NOT be used in the FRONT page of the business card.

```html
<!DOCTYPE html>
<html lang="en">
<head>
<meta charset="utf-8">
<title>Milo Verhagen — Business Card</title>
<link href="https://fonts.googleapis.com/css2?family=Noto+Serif:wght@400&family=Arimo:wght@400&display=swap" rel="stylesheet">
<style>
  :root {
    --page-bg: #ffffff;
    --ink: #1a1a1a;
    --card-border: #222222;
    --marble-dark: #050505;
    --marble-mid: #1b1b1b;
    --marble-vein: #3a3a36;
    --watermark-ink: #1f1f1f;
  }
  * { margin: 0; padding: 0; box-sizing: border-box; }
  html, body {
    width: 1200px;
    height: 1200px;
    overflow: hidden;
    background: var(--page-bg);
  }
  .canvas {
    position: relative;
    width: 1200px;
    height: 1200px;
  }
  .card {
    position: absolute;
    left: 343px;
    width: 508px;
    height: 290px;
  }
  .card-front {
    top: 270px;
    background:
      radial-gradient(ellipse 60% 18% at 45% 8%, var(--marble-vein), transparent 70%),
      linear-gradient(160deg, var(--marble-mid) 0%, var(--marble-dark) 45%, var(--marble-mid) 80%, var(--marble-dark) 100%);
  }
  .card-front .marble {
    position: absolute;
    inset: 0;
  }
  .front-mark {
    position: absolute;
    top: 50%;
    left: 50%;
    transform: translate(-50%, -50%);
    font-family: "Noto Serif", serif;
    font-size: 27px;
    letter-spacing: 1px;
    text-transform: uppercase;
    color: var(--watermark-ink);
    white-space: nowrap;
  }
  .card-back {
    top: 632px;
    background: var(--page-bg);
    border: 1px solid var(--card-border);
  }
  .back-content {
    position: absolute;
    right: 101px;
    top: 66px;
    text-align: right;
    color: var(--ink);
  }
  .brand-name {
    font-family: "Noto Serif", serif;
    font-size: 16px;
    letter-spacing: 0.5px;
    text-transform: uppercase;
    line-height: 1;
    white-space: nowrap;
  }
  .person-name {
    margin-top: 40px;
    font-family: "Noto Serif", serif;
    font-size: 20px;
    line-height: 1;
  }
  .phone {
    margin-top: 17px;
    font-family: "Noto Serif", serif;
    font-size: 15px;
    line-height: 1;
  }
  .web-links {
    margin-top: 15px;
    font-family: "Arimo", sans-serif;
    font-size: 12.5px;
    line-height: 13px;
  }
</style>
</head>
<body>
  <main class="canvas">
    <section class="card card-front">
      <div class="marble" role="img" aria-label="Black marble texture with fine white veins"></div>
      <div class="front-mark">Milo Verhagen</div>
    </section>

    <section class="card card-back">
      <div class="back-content">
        <div class="brand-name">Milo Verhagen</div>
        <div class="person-name">Milo Reeb</div>
        <div class="phone">+614 27 305 641</div>
        <div class="web-links">
          <div>www.miloverhagen.com.au</div>
          <div>milo@miloverhagen.com.au</div>
        </div>
      </div>
    </section>
  </main>
</body>
</html>
```